Legislative compliance to home owners, landlords and agents

Logo, business card and stationaly header for a sole trader offering sevices in the UK to home owners, landlords and Letting agents to meet legislation requirement relating to sale and leasing of rental domestic homes. Services offered include Legionella Risk Assessment, Portable Appliance Testing and Energy Performance Certificates. Logo to include depiction of a house and compliance tick list images. Have an existing card with water splash image to reflect water testing, so considering picking up same wave blue. Company name Kestov Property Services. Web www.kestovps-example.com. email: info@kestovps-example.com. Address: Brackenlea, Aberdeen. All three services to be listed. Name as existing card.,

Target Market(s)

UK home owners, landlords, lettings and estate agents

Industry/Entity Type

Property Management

Contact Information for Business Card

Derek Moffatt CEng, MSFabTec
Address: Brackenlea, Aberdeen
Web: www.kestovps-example.com
e-mail info@kestovps-example.com
Phone: 07700 918 302
Services: Legionella Risk Assessment, Portable Appliance Testing, Energy Performance Certificate

Logo Text

Kestov Property Services

Font styles to use
Sans Serif

Colors

Designer to choose colors to be used in the design.

Requirements
Must have
• Suitable for standard UK business card size 85 mm x 55 mm, with allowance for safety border/ bleed such that colours extend to outside border of card once printed
Nice to have
• Clear font style and layout
• Happy to see images depicting phone, address etc

```html
<!DOCTYPE html>
<html lang="en">
<head>
<meta charset="utf-8">
<title>Kestov Property Services – Business Card</title>
<link rel="stylesheet" href="https://fonts.googleapis.com/css2?family=Open+Sans:wght@400;600&family=Crimson+Pro:wght@600;700&display=swap">
<style>
  :root {
    --navy: #08106b;
    --sky: #27a8e0;
    --leaf: #5cc23a;
    --paper: #ffffff;
    --ink: #1c1f3a;
    --backdrop: #eceae6;
    --card-w: 540px;
    --card-h: 349px;
  }
  * { box-sizing: border-box; margin: 0; padding: 0; }
  html, body {
    width: 1200px; height: 900px; overflow: hidden;
    background: var(--backdrop);
  }
  .sheet {
    position: relative; width: 1200px; height: 900px;
    display: flex; align-items: center; justify-content: center; gap: 40px;
  }
  .card {
    position: relative; width: var(--card-w); height: var(--card-h);
    overflow: hidden; box-shadow: 0 6px 18px rgba(0,0,0,.18);
  }
  .card--front {
    background: var(--navy);
    display: flex; align-items: center; justify-content: center;
  }
  .brand {
    font-family: "Open Sans", sans-serif; font-weight: 600;
    text-align: center; line-height: 1.1;
  }
  .card--front .brand { color: var(--paper); font-size: 40px; letter-spacing: 1px; }
  .card--front .brand small { display: block; font-size: 24px; letter-spacing: .5px; }
  .card--back { background: var(--paper); }
  .card__wave { position: absolute; inset: 0; width: 100%; height: 100%; }
  .card--back .brand {
    position: absolute; top: 40px; right: 30px;
    color: var(--navy); font-size: 30px; text-align: center;
    display: flex; align-items: center; gap: 8px;
  }
  .card--back .brand small { display: block; font-size: 16px; }
  .brand__dot { width: 12px; height: 12px; border-radius: 50%; background: var(--leaf); flex: none; }
  .holder {
    position: absolute; top: 38px; left: 36px;
    font-family: "Crimson Pro", serif; color: var(--navy);
    font-size: 24px; font-weight: 700;
  }
  .holder__post { font-size: 15px; font-weight: 600; margin-left: 4px; }
  .contacts {
    position: absolute; top: 96px; left: 38px; list-style: none;
    font-family: "Open Sans", sans-serif; font-size: 14px; color: var(--ink);
  }
  .contacts li { display: flex; align-items: center; gap: 8px; height: 21px; }
  .contacts svg { width: 11px; height: 11px; fill: var(--navy); }
  .services {
    position: absolute; top: 170px; left: 38px; list-style: none;
    font-family: "Open Sans", sans-serif; font-size: 15px; color: var(--ink);
  }
  .services li { display: flex; align-items: center; gap: 8px; height: 22px; }
  .services svg { width: 14px; height: 12px; }
  .address {
    position: absolute; right: 18px; top: 232px;
    font-family: "Open Sans", sans-serif; font-size: 12px; color: var(--paper);
    white-space: nowrap;
  }
</style>
</head>
<body>
<main class="sheet">
  <section class="card card--front" aria-label="Card front">
    <div class="brand">Kestov<small>Property Services</small></div>
  </section>

  <section class="card card--back" aria-label="Card back">
    <svg class="card__wave" viewBox="0 0 540 349" preserveAspectRatio="none" aria-hidden="true">
      <path d="M0,300 C150,330 300,260 540,120 L540,349 L0,349 Z" fill="var(--sky)"/>
      <path d="M0,280 C160,312 320,250 470,160 C330,255 170,302 0,292 Z" fill="var(--leaf)"/>
    </svg>

    <div class="brand"><span class="brand__dot"></span><div>Kestov<small>Property Services</small></div></div>

    <h1 class="holder">Derek Moffatt<span class="holder__post">CEng, MSFabTec</span></h1>

    <ul class="contacts">
      <li><svg viewBox="0 0 24 24"><path d="M6.6 10.8a15 15 0 0 0 6.6 6.6l2.2-2.2a1 1 0 0 1 1-.25 11.4 11.4 0 0 0 3.6.57 1 1 0 0 1 1 1V20a1 1 0 0 1-1 1A17 17 0 0 1 3 4a1 1 0 0 1 1-1h3.5a1 1 0 0 1 1 1c0 1.25.2 2.45.57 3.57a1 1 0 0 1-.25 1z"/></svg>07700 918 302</li>
      <li><svg viewBox="0 0 24 24"><path d="M2 5h20v14H2z M2 5l10 8 10-8" /></svg>info@kestovps-example.com</li>
      <li><svg viewBox="0 0 24 24"><circle cx="12" cy="12" r="10"/></svg>www.kestovps-example.com</li>
    </ul>

    <ul class="services">
      <li><svg viewBox="0 0 14 12"><path d="M1 6l4 4 8-9" fill="none" stroke="var(--leaf)" stroke-width="2.4"/></svg>Legionella Risk Assessment</li>
      <li><svg viewBox="0 0 14 12"><path d="M1 6l4 4 8-9" fill="none" stroke="var(--leaf)" stroke-width="2.4"/></svg>Portable Appliance Testing</li>
      <li><svg viewBox="0 0 14 12"><path d="M1 6l4 4 8-9" fill="none" stroke="var(--leaf)" stroke-width="2.4"/></svg>Energy Performance Certificate</li>
    </ul>

    <p class="address">Brackenlea, Aberdeen</p>
  </section>
</main>
</body>
</html>
```